Flyer Design Project

asphalt paving company needs 3 designs for inserts to place inside presentation folder. I will up load samples of basic concept and information required but needs to be completely redesigned. Looking for professional modern look.

Industry/Entity Type

It Company

```html
<!DOCTYPE html>
<html lang="en">
<head>
<meta charset="utf-8">
<title>Thinking Outside the Box – Folder Insert</title>
<link rel="stylesheet" href="https://fonts.googleapis.com/css2?family=Alegreya:ital,wght@0,400;1,400&display=swap">
<style>
  :root {
    --paper: #fffdf9;
    --ink: #1f1c1a;
    --rule: #d9d6d2;
    --peach: #f7c58f;
    --peach-soft: #fbe3c6;
    --peach-faint: #fff4e8;
    --sky-deep: #4e6fa8;
    --sky-mid: #7f9fcf;
    --sky-light: #b9cde8;
  }
  html, body {
    margin: 0;
    padding: 0;
    overflow: hidden;
    background: var(--paper);
  }
  .insert {
    position: relative;
    width: 848px;
    height: 1200px;
    overflow: hidden;
    background: var(--paper);
    font-family: "Alegreya", Georgia, serif;
    color: var(--ink);
  }
  .dot-field {
    position: absolute;
    top: 0;
    left: 0;
    width: 848px;
    height: 300px;
    background:
      radial-gradient(ellipse 520px 230px at 560px 70px, var(--peach) 0%, var(--peach-soft) 45%, rgba(255,244,232,0) 80%),
      linear-gradient(to right, var(--paper) 0%, var(--peach-faint) 40%, var(--paper) 100%);
  }
  .line-sweep {
    position: absolute;
    left: 0;
    bottom: 0;
    width: 848px;
    height: 620px;
    background:
      radial-gradient(ellipse 520px 300px at 300px 560px, rgba(247,197,143,0.35) 0%, rgba(251,227,198,0.18) 50%, rgba(255,253,249,0) 80%),
      radial-gradient(ellipse 380px 420px at 760px 250px, rgba(247,197,143,0.22) 0%, rgba(255,253,249,0) 75%);
  }
  .hero-photo {
    position: absolute;
    left: 110px;
    top: 190px;
    width: 640px;
    height: 425px;
    border-radius: 34px 0 64px 0;
    background: linear-gradient(160deg, var(--sky-deep) 0%, var(--sky-mid) 55%, var(--sky-light) 100%);
  }
  .divider {
    position: absolute;
    left: 148px;
    top: 676px;
    width: 550px;
    height: 1px;
    background: var(--rule);
  }
  .copy {
    position: absolute;
    left: 120px;
    top: 692px;
    width: 610px;
    font-size: 27.5px;
    line-height: 38.5px;
    text-align: justify;
  }
  .copy p {
    margin: 0 0 38px;
  }
  .lead-in {
    letter-spacing: 0.12em;
    font-size: 25px;
  }
  .call-to-action {
    font-style: italic;
    text-align: left;
  }
</style>
</head>
<body>
  <main class="insert">
    <div class="dot-field" role="img" aria-label="Decorative field of soft orange dots fading across the top"></div>
    <div class="line-sweep" role="img" aria-label="Decorative sweep of fine peach curved lines"></div>
    <div class="hero-photo" role="img" aria-label="Businessman in a suit tossing an open cardboard box into a blue sky"></div>
    <div class="divider"></div>
    <section class="copy">
      <p><span class="lead-in">THE MOST CRITICAL COMPONENT</span> of our success has been thinking outside the box, so we decided to throw out the box.</p>
      <p>With our resourceful and creative approach, you are guaranteed to receive the highest level of quality and customer service at unbeatable prices, regardless of job size, budget, scope of work, or city.</p>
      <p class="call-to-action">Call us today and see for yourself.</p>
    </section>
  </main>
</body>
</html>
```